businesscard, flyer and membercard

--------------------------------------------------------------------------------------------------
design flyer :
- delivering format (jpg, pdf and original psd)
- there is a example how the flyers should look like
the text and logo should be the same as the exemple flyer, the creativity is yours.
- the design should have a back and front side.
File format : 15,0 cm x 21,2 cm
design membercard :
- there is example how the member-card should look like
the text and logo should be the same as the exemple membercard, the creativity is yours.
- the front side contains text and open space where for writing :
Naam ......
Dansstijlen ......
- the front side contains 12 circels horizontal at the line name at the end of the line "Salsa".
- the front side contains 12 circels horizontal at the line name at the end of the line "Bachata".
- the front side contains 12 circels horizontal at the line name at the end of the line "Kizomba".
- each horizontal line with circels contains a different kind of color/design.
- file format: 7,6 cm x 10,7 cm
Business card :
- there is example how the businesscard should look like
the text and logo should be the same as the exemple buisinesscard, the creativity is yours.
- the design should have a back a front side
File format : 8,7 cm x 5,7 cm

Target Market(s)

Dancing :Salsa, Bachata and Kizomba

Colors

Designer to choose colors to be used in the design.

Requirements
Must have
• same text as seen on the examples.
Nice to have
• see the examples as attachments
Should not have
• - REMOVE TEXT "KOV" from the design
• - REMOVE TEXT "Gratis Parkeren"

```html
<!DOCTYPE html>
<html lang="nl">
<head>
<meta charset="utf-8">
<title>Nova Dance Studio – flyer en ledenkaart</title>
<link href="https://fonts.googleapis.com/css2?family=Raleway:wght@500;600;800&family=Montserrat:wght@500;600&display=swap" rel="stylesheet">
<style>
  :root{
    --board-light:#d1d3d4;
    --board-dark:#3c3c3d;
    --card-deep:#1e0e22;
    --card-violet:#4a1d6e;
    --card-blue:#5e8fd0;
    --card-red:#d8264a;
    --white:#ffffff;
    --stamp-red:#e0202a;
  }
  *{margin:0;padding:0;box-sizing:border-box}
  html,body{width:843px;height:1200px;overflow:hidden}
  body{
    position:relative;
    background:linear-gradient(to bottom,var(--board-light) 0 963px,var(--board-dark) 963px 100%);
    font-family:"Raleway",sans-serif;color:var(--white);
  }
  .card{
    position:absolute;left:95px;width:653px;height:428px;overflow:hidden;
    background:
      radial-gradient(ellipse 220px 260px at 330px 180px,rgba(94,143,208,.75),transparent 70%),
      radial-gradient(ellipse 260px 220px at 650px 260px,rgba(216,38,74,.7),transparent 70%),
      linear-gradient(100deg,var(--card-deep) 0%,#2c1240 30%,var(--card-violet) 55%,#7a2a6a 100%);
  }
  .card--flyer{top:153px}
  .card--member{top:619px;height:427px}
  .photo{
    position:absolute;right:0;top:0;width:380px;height:100%;
    background:
      radial-gradient(ellipse 90px 230px at 200px 200px,rgba(20,8,20,.85),transparent 75%),
      radial-gradient(ellipse 120px 150px at 300px 230px,rgba(150,20,40,.55),transparent 75%);
  }
  .brand{position:absolute;left:20px;top:44px;width:226px;text-align:center}
  .brand__name{display:flex;align-items:center;justify-content:center;gap:8px;
    font-weight:600;font-size:36px;letter-spacing:4px;line-height:1}
  .brand__dot{width:12px;height:12px;border-radius:50%;background:var(--stamp-red)}
  .brand__studio{margin-top:62px;font-weight:600;font-size:17px;letter-spacing:.5px;line-height:1.1}
  .brand__tagline{font-size:4px;letter-spacing:.6px;text-transform:uppercase;margin-top:1px}
  .styles{position:absolute;left:35px;top:205px;font-weight:800;font-size:51px;line-height:63px}
  .contact{position:absolute;right:26px;top:322px;text-align:right;
    font-family:"Montserrat",sans-serif;font-weight:500;font-size:14px;line-height:19px}
  .contact li{list-style:none;display:flex;justify-content:flex-end;align-items:center;gap:4px}
  .contact svg{width:14px;height:14px}
  .field{position:absolute;left:35px;font-weight:600;font-size:17px;display:flex;align-items:flex-end;gap:6px}
  .field__line{display:block;border-bottom:1px solid var(--white);height:1px;margin-bottom:4px}
  .field--name{top:190px}.field--name .field__line{width:202px}
  .field--styles{top:222px}.field--styles .field__line{width:168px}
  .stamps{position:absolute;left:0;top:0}
  .footer{position:absolute;left:35px;top:389px;font-family:"Montserrat",sans-serif;font-weight:600;font-size:16.5px}
</style>
</head>
<body>

<section class="card card--flyer">
  <div class="photo" role="img" aria-label="Foto van een dansend paar in avondkleding, man in pak en vrouw in lange zwarte jurk"></div>
  <div class="brand">
    <div class="brand__name"><span>NOVA</span><span class="brand__dot"></span></div>
    <div class="brand__studio">DANCE STUDIO</div>
    <div class="brand__tagline">Feel the rhythm, move as one</div>
  </div>
  <h1 class="styles">SALSA<br>BACHATA &amp;<br>KIZOMBA</h1>
  <ul class="contact">
    <li>0612 480 375
      <svg viewBox="0 0 14 14"><circle cx="7" cy="7" r="6.2" fill="none" stroke="#fff" stroke-width="1.2"/><path d="M4.6 3.8l1.3 1.6-.7.9c.5 1 1.2 1.8 2.3 2.4l.9-.7 1.6 1.3-.8 1.1C6.6 10 4.2 7.6 3.6 4.6z" fill="#fff"/></svg></li>
    <li>novadenhaag@mailbox.nl
      <svg viewBox="0 0 14 14"><circle cx="7" cy="7" r="6.2" fill="none" stroke="#fff" stroke-width="1.2"/><rect x="3.6" y="4.8" width="6.8" height="4.6" fill="none" stroke="#fff" stroke-width="1"/><path d="M3.6 4.8L7 7.6l3.4-2.8" fill="none" stroke="#fff" stroke-width="1"/></svg></li>
    <li>novadenhaag
      <svg viewBox="0 0 14 14"><circle cx="7" cy="7" r="6.2" fill="none" stroke="#fff" stroke-width="1.2"/></svg></li>
  </ul>
</section>

<section class="card card--member">
  <div class="photo" role="img" aria-label="Foto van een dansend paar in avondkleding, man in pak en vrouw in lange zwarte jurk"></div>
  <div class="brand">
    <div class="brand__name"><span>NOVA</span><span class="brand__dot"></span></div>
    <div class="brand__studio">DANCE STUDIO</div>
    <div class="brand__tagline">Feel the rhythm, move as one</div>
  </div>
  <div class="field field--name">Naam <span class="field__line"></span></div>
  <div class="field field--styles">Dansstijlen <span class="field__line"></span></div>
  <svg class="stamps" width="653" height="427" viewBox="0 0 653 427" font-family="Montserrat, sans-serif" font-weight="600" text-anchor="middle" fill="#e0202a">
    <g stroke="#e0202a" stroke-width="2" fill="#fff">
      <circle cx="63" cy="286" r="30"/><circle cx="126" cy="286" r="27"/><circle cx="182" cy="286" r="24"/><circle cx="234" cy="286" r="22"/><circle cx="281" cy="286" r="19"/><circle cx="323" cy="286" r="17"/><circle cx="364" cy="286" r="15"/>
      <circle cx="63" cy="351" r="30"/><circle cx="126" cy="351" r="27"/><circle cx="182" cy="351" r="24"/><circle cx="234" cy="351" r="22"/><circle cx="281" cy="351" r="19"/><circle cx="323" cy="351" r="17"/><circle cx="364" cy="351" r="15"/>
    </g>
    <g font-size="30"><text x="63" y="297">1</text><text x="63" y="362">1</text></g>
    <g font-size="27"><text x="126" y="296">2</text><text x="126" y="361">2</text></g>
    <g font-size="25"><text x="182" y="295">3</text><text x="182" y="360">3</text></g>
    <g font-size="23"><text x="234" y="294">4</text><text x="234" y="359">4</text></g>
    <g font-size="21"><text x="281" y="293">5</text><text x="281" y="358">5</text></g>
    <g font-size="19"><text x="323" y="293">6</text><text x="323" y="358">6</text></g>
    <g font-size="18"><text x="364" y="292">7</text><text x="364" y="357">7</text></g>
  </svg>
  <p class="footer">Parkweg 24, 2511 AB Den Haag | Fb: Novadenhaag | Ph:0612480375</p>
</section>

</body>
</html>
```